Business Card Design Project

Hello,

We have just created our new COMPANY LOGO via Pixel Harbor and would not like to turn our attention to new Business Cards.

We are a printing company based in Singapore & Las Vegas. We specialize in blue-print printing for the Architectural, Engineering and Construction industries

The design should be simple, professional, clean and organized.

The Business Cards should "pop" when seen and will hopefully be something that makes you look twice.

We have two different Pan-tones that we use for our company, feel free to use them if you think they will work for your design?

Orange: PMS 021
Gray: PMS 431

I have attached our current logo for your use and reference which should obvious be on our business cards.

Considering we have two locations on different continents, we need business cards templates where the address details need to be interchangeable for each different location (total 2)

First one:
38 Merrow Lane #03-11 to #03-15
Singapore 528473
Tel : +65 6847-3920
Fax : +65 6843-7702

Second one:
2381 W. Tanfield Rd, Suite 204
Las Vegas, Nevada 89152
Tel : (702) 555-4137
Fax : (702) 555-4189

We would also like to list a few of our key services on the card. Here are a few examples to get you going.

Plan Printing & Plotting
Digital Colour Printing
Cadline Printing
Specialty Book Making
Scanning & Archiving
Collection & Delivey

This is the first time i have requested for business cards to be created so please let me know if you require any additional information.
Many Thanks,
Tobin
Updates

Project Deadline Extended
Reason: It took us longer than expected to finalize our Company Logo We look forward to receiving your designs.

Target Market(s)

Our Target Market is construction related people.
Construction
Architecture
Engineering

Industry/Entity Type

Printing

Font styles to use
Other font styles liked:
• Times New Roman

Colors
faa54b
ffffff

Requirements
Must have
• The business card must have our Company Logo (attached)
The font used must be Times New Roman
Should not have
• Playful images of print designs and/or logos

```html
<!DOCTYPE html>
<html lang="en">
<head>
<meta charset="utf-8">
<title>Norvale Print Works – Business Cards</title>
<link rel="stylesheet" href="https://fonts.googleapis.com/css2?family=Tinos:ital,wght@0,400;0,700;1,400&family=Arimo:wght@400&display=swap">
<style>
  :root {
    --orange: #f5a24b;
    --white: #ffffff;
    --ink: #111114;
    --panel: #0e0e12;
    --gray-light: #c9c9c9;
    --gray-dark: #6f6f6f;
    --stage: #ebebeb;
  }
  html, body {
    margin: 0;
    padding: 0;
    width: 1037px;
    height: 1200px;
    overflow: hidden;
    background: var(--stage);
  }
  .sheet {
    width: 1037px;
    height: 1200px;
    display: flex;
    flex-direction: column;
    align-items: center;
    justify-content: space-evenly;
  }
  .card {
    display: block;
    width: 620px;
    height: 340px;
    background: var(--white);
    box-shadow: 0 4px 14px rgba(0,0,0,0.18);
  }
  .serif { font-family: "Tinos", "Times New Roman", serif; }
  .sans { font-family: "Arimo", Arial, sans-serif; }
  .brand-mark { fill: var(--orange); font-size: 74px; letter-spacing: 2px; }
  .brand-mark--dark { fill: var(--ink); font-size: 40px; }
  .company-name { fill: var(--ink); font-size: 18px; font-weight: 700; }
  .company-tagline { fill: var(--ink); font-size: 12.5px; font-style: italic; }
  .holder-name { fill: var(--ink); font-size: 15.5px; }
  .holder-title { fill: var(--ink); font-size: 9px; font-style: italic; }
  .contact-number { fill: var(--ink); font-size: 11.5px; }
  .contact-number--light { fill: var(--white); }
  .service-item { fill: var(--orange); font-size: 11.5px; }
  .service-bullet { fill: var(--white); }
  .address-line { fill: var(--orange); font-size: 11px; }
</style>
</head>
<body>
<main class="sheet">

  <!-- Front -->
  <svg class="card card--front" viewBox="0 0 505 277" aria-label="Card front">
    <rect width="505" height="277" fill="var(--white)"/>
    <text class="brand-mark serif" x="252.5" y="164" text-anchor="middle">NPW</text>
    <rect x="0" y="260" width="505" height="17" fill="var(--orange)"/>
  </svg>

  <!-- Back: Singapore -->
  <svg class="card card--back" viewBox="0 0 505 277" aria-label="Card back, Singapore office">
    <rect width="505" height="277" fill="var(--white)"/>
    <text class="brand-mark--dark serif" x="151" y="52" text-anchor="middle">NPW</text>
    <text class="company-name serif" x="151" y="82" text-anchor="middle">Norvale Print Works</text>
    <text class="company-tagline serif" x="151" y="101" text-anchor="middle">A Member of the Norvale Group of Companies</text>
    <rect x="0" y="116" width="315" height="2" fill="var(--orange)"/>
    <rect x="417" y="116" width="88" height="2" fill="var(--orange)"/>
    <text class="holder-name serif" x="333" y="121">Mira Tolle</text>
    <text class="holder-title serif" x="333" y="136">Managing Director</text>
    <polygon points="0,148 283,148 275,165 0,165" fill="var(--gray-light)"/>
    <polygon points="283,148 505,148 505,165 275,165" fill="var(--gray-dark)"/>
    <g class="icon-phone" fill="var(--ink)">
      <rect x="22" y="153" width="12" height="8" rx="1.5"/>
      <rect x="20" y="151" width="16" height="3" rx="1.5"/>
    </g>
    <text class="contact-number sans" x="48" y="161">+65 6847-3920</text>
    <g class="icon-fax" fill="var(--white)">
      <rect x="335" y="151" width="8" height="3"/>
      <rect x="332" y="154" width="14" height="6" rx="1"/>
      <rect x="335" y="160" width="8" height="2"/>
    </g>
    <text class="contact-number contact-number--light sans" x="352" y="161">+65 6843-7702</text>
    <rect x="0" y="165" width="505" height="112" fill="var(--panel)"/>
    <g class="service-list">
      <circle class="service-bullet" cx="29" cy="189" r="3"/>
      <text class="service-item sans" x="50" y="193">Plan Printing &amp; Plotting</text>
      <circle class="service-bullet" cx="29" cy="206" r="3"/>
      <text class="service-item sans" x="50" y="210">Digital Colour Printing</text>
      <circle class="service-bullet" cx="29" cy="223" r="3"/>
      <text class="service-item sans" x="50" y="227">Cadline Printing</text>
      <circle class="service-bullet" cx="29" cy="240" r="3"/>
      <text class="service-item sans" x="50" y="244">Specialty Book Making</text>
      <circle class="service-bullet" cx="29" cy="257" r="3"/>
      <text class="service-item sans" x="50" y="261">Scanning &amp; Archiving</text>
      <circle class="service-bullet" cx="29" cy="274" r="0"/>
    </g>
    <text class="service-item sans" x="50" y="276" display="none"></text>
    <text class="address-line sans" x="494" y="261" text-anchor="end">38 Merrow Lane #03-11 to #03-15 Singapore 528473</text>
  </svg>

  <!-- Back: Las Vegas -->
  <svg class="card card--back" viewBox="0 0 505 277" aria-label="Card back, Las Vegas office">
    <rect width="505" height="277" fill="var(--white)"/>
    <text class="brand-mark--dark serif" x="151" y="52" text-anchor="middle">NPW</text>
    <text class="company-name serif" x="151" y="82" text-anchor="middle">Norvale Print Works</text>
    <text class="company-tagline serif" x="151" y="101" text-anchor="middle">A Member of the Norvale Group of Companies</text>
    <rect x="0" y="116" width="315" height="2" fill="var(--orange)"/>
    <rect x="417" y="116" width="88" height="2" fill="var(--orange)"/>
    <text class="holder-name serif" x="333" y="121">Mira Tolle</text>
    <text class="holder-title serif" x="333" y="136">Managing Director</text>
    <polygon points="0,148 283,148 275,165 0,165" fill="var(--gray-light)"/>
    <polygon points="283,148 505,148 505,165 275,165" fill="var(--gray-dark)"/>
    <g class="icon-phone" fill="var(--ink)">
      <rect x="22" y="153" width="12" height="8" rx="1.5"/>
      <rect x="20" y="151" width="16" height="3" rx="1.5"/>
    </g>
    <text class="contact-number sans" x="48" y="161">(702) 555-4137</text>
    <g class="icon-fax" fill="var(--white)">
      <rect x="335" y="151" width="8" height="3"/>
      <rect x="332" y="154" width="14" height="6" rx="1"/>
      <rect x="335" y="160" width="8" height="2"/>
    </g>
    <text class="contact-number contact-number--light sans" x="352" y="161">(702) 555-4189</text>
    <rect x="0" y="165" width="505" height="112" fill="var(--panel)"/>
    <g class="service-list">
      <circle class="service-bullet" cx="29" cy="184" r="3"/>
      <text class="service-item sans" x="50" y="188">Plan Printing &amp; Plotting</text>
      <circle class="service-bullet" cx="29" cy="201" r="3"/>
      <text class="service-item sans" x="50" y="205">Digital Colour Printing</text>
      <circle class="service-bullet" cx="29" cy="218" r="3"/>
      <text class="service-item sans" x="50" y="222">Cadline Printing</text>
      <circle class="service-bullet" cx="29" cy="235" r="3"/>
      <text class="service-item sans" x="50" y="239">Specialty Book Making</text>
      <circle class="service-bullet" cx="29" cy="252" r="3"/>
      <text class="service-item sans" x="50" y="256">Scanning &amp; Archiving</text>
      <circle class="service-bullet" cx="29" cy="269" r="3"/>
      <text class="service-item sans" x="50" y="273">Collection &amp; Delivey</text>
    </g>
    <text class="address-line sans" x="494" y="273" text-anchor="end">2381 W. Tanfield Rd, Suite 204 Las Vegas, Nevada 89152</text>
  </svg>

</main>
</body>
</html>
```